Quote Cards for Social Media RV

I would like to put these quotes over one of the pictures attached; One Quote per picture, and I want the quote to be bold or easy to read as well. I provided a few reference graphics that I really like as examples below. In very small letters at the bottom add @RVCarloweDaily

All of the pictures are attached; you can pick any photo and add one quote to it; but no stock photography

Target Market(s)

women trying to lose weight

Requirements
Must have
• quotes and pictures attached
Should not have
• no stock photography

```html
<!DOCTYPE html>
<html lang="en">
<head>
<meta charset="utf-8">
<title>RV Quote Cards</title>
<link rel="stylesheet" href="https://fonts.googleapis.com/css2?family=Poppins:wght@700;800&display=swap">
<style>
  :root {
    --page: #ffffff;
    --ink: #ffffff;
    --handle: #f7dc1b;
    --navy-deep: #0b0f3d;
    --navy: #1c1f86;
    --shadow: rgba(0, 0, 0, 0.55);
  }
  * { box-sizing: border-box; margin: 0; padding: 0; }
  html, body {
    width: 677px; height: 1200px; overflow: hidden;
    background: var(--page);
  }
  .board { position: relative; width: 677px; height: 1200px; }
  .quote-card {
    position: absolute; overflow: hidden;
    font-family: "Poppins", sans-serif;
    color: var(--ink);
  }
  .quote-card .photo { position: absolute; inset: 0; }
  .quote-card .quote {
    position: absolute; left: 6%; right: 6%;
    font-weight: 700; line-height: 1.18;
    text-align: center;
    text-shadow: 0 1px 4px var(--shadow);
  }
  .quote-card .handle {
    position: absolute; left: 0; right: 0; bottom: 4%;
    font-weight: 800; font-size: 10px;
    color: var(--handle); text-align: center;
    text-shadow: 0 1px 2px var(--shadow);
  }

  .card-lied     { left: 17px;  top: 11px;  width: 196px; height: 199px; }
  .card-stubborn { left: 224px; top: 11px;  width: 181px; height: 219px; }
  .card-hormones { left: 416px; top: 11px;  width: 242px; height: 377px; }
  .card-frustrated { left: 15px; top: 240px; width: 198px; height: 293px; }
  .card-natural  { left: 224px; top: 240px; width: 182px; height: 234px; }
  .card-supplement { left: 416px; top: 398px; width: 245px; height: 326px; }
  .card-glp      { left: 15px;  top: 542px; width: 200px; height: 285px; }
  .card-struggling { left: 224px; top: 483px; width: 182px; height: 245px; }
  .card-boost    { left: 224px; top: 737px; width: 183px; height: 250px; }
  .card-tomorrow { left: 415px; top: 733px; width: 246px; height: 413px; }

  .card-lied .photo { background: linear-gradient(180deg, #6f9fd0 0%, #9fb7c9 35%, #3f5c34 70%, #22361e 100%); }
  .card-lied .quote { top: 30%; font-size: 15.5px; }

  .card-stubborn .photo { background: linear-gradient(180deg, #7fa6d6 0%, #a9bccb 38%, #4a6a3c 70%, #24361d 100%); }
  .card-stubborn .quote { top: 36%; left: 30%; right: 5%; text-align: right; font-size: 14.5px; }
  .card-stubborn .handle { text-align: right; padding-right: 6%; }

  .card-hormones .photo { background: linear-gradient(180deg, #2a2522 0%, #3b3634 40%, #5a4a3b 75%, #8a7257 100%); }
  .card-hormones .quote { top: 48%; font-size: 19px; }

  .card-frustrated .photo { background: radial-gradient(ellipse at 60% 35%, #2a2fb0 0%, var(--navy) 40%, var(--navy-deep) 100%); }
  .card-frustrated .quote { top: 34%; left: 4%; right: 4%; font-size: 16px; }

  .card-natural .photo { background: linear-gradient(180deg, #d9d9d9 0%, #bdbdbd 30%, #3a3a3a 60%, #111111 100%); }
  .card-natural .quote { top: 45%; font-size: 13.5px; }

  .card-supplement .photo { background: linear-gradient(180deg, #3a342f 0%, #2a2521 45%, #1a1715 100%); }
  .card-supplement .quote { top: 41%; left: 3%; right: 3%; font-size: 20.5px; }

  .card-glp .photo { background: radial-gradient(ellipse at 50% 30%, #2b2f9e 0%, var(--navy) 35%, var(--navy-deep) 100%); }
  .card-glp .quote { top: 26%; left: 3%; right: 3%; font-size: 16px; }

  .card-struggling .photo { background: linear-gradient(180deg, #e3ddd4 0%, #cdbfae 30%, #4a4038 65%, #141210 100%); }
  .card-struggling .quote { top: 39%; font-size: 13.5px; }

  .card-boost .photo { background: linear-gradient(135deg, #d9632a 0%, #a8326e 40%, #4a1f7a 70%, #1b1240 100%); }
  .card-boost .quote { top: 38%; font-size: 14.5px; }

  .card-tomorrow .photo { background: radial-gradient(circle at 45% 35%, #b23a4e 0%, #6a2a8a 35%, #2a1a6e 60%, #0f0b45 100%); }
  .card-tomorrow .quote { top: 53%; left: 6%; right: 6%; font-size: 19px; }
  .card-tomorrow .handle { bottom: 5%; }
</style>
</head>
<body>
<main class="board">
  <article class="quote-card card-lied">
    <div class="photo" role="img" aria-label="Photo of RV smiling outdoors on a hillside under blue sky"></div>
    <p class="quote">“You've been lied to - 'just eat less and exercise more' doesn't work in menopause”</p>
    <p class="handle">@RVCarloweDaily</p>
  </article>

  <article class="quote-card card-stubborn">
    <div class="photo" role="img" aria-label="Photo of RV in black outfit posing on a hillside"></div>
    <p class="quote">“That stubborn belly fat isn't your fault - here's what no one tells you.”</p>
    <p class="handle">@RVCarloweDaily</p>
  </article>

  <article class="quote-card card-hormones">
    <div class="photo" role="img" aria-label="Photo of RV in a sheer black outfit standing by a city-view window"></div>
    <p class="quote">“Sis, your hormones are out of whack - that's why the weight won't budge!”</p>
    <p class="handle">@RVCarloweDaily</p>
  </article>

  <article class="quote-card card-frustrated">
    <div class="photo" role="img" aria-label="Photo of RV in a purple dress on a deep blue backdrop"></div>
    <p class="quote">“Frustrated with belly fat that won't budge? I've got the solution that finally worked for me-no crazy diets required.”</p>
    <p class="handle">@RVCarloweDaily</p>
  </article>

  <article class="quote-card card-natural">
    <div class="photo" role="img" aria-label="Photo of RV dancing in a white sweater in a bright room"></div>
    <p class="quote">“Finally-a natural solution that flattens your belly AND eases stomach bloat”</p>
    <p class="handle">@RVCarloweDaily</p>
  </article>

  <article class="quote-card card-supplement">
    <div class="photo" role="img" aria-label="Photo of RV smiling in a striped sheer black top indoors"></div>
    <p class="quote">“One supplement, one night; your belly bloat could be gone by morning. Here's how it works!”</p>
    <p class="handle">@RVCarloweDaily</p>
  </article>

  <article class="quote-card card-glp">
    <div class="photo" role="img" aria-label="Photo of RV in a brown turtleneck on a deep blue backdrop"></div>
    <p class="quote">“• GLP-1: the magic behind the weight loss drugs. But here's the secret - you can boost it naturally without a prescription!”</p>
    <p class="handle">@RVCarloweDaily</p>
  </article>

  <article class="quote-card card-struggling">
    <div class="photo" role="img" aria-label="Photo of RV laughing in a beige turtleneck against a stone wall"></div>
    <p class="quote">“Struggling with bloating and belly fat? Try this natural solution tonight, and wake up feeling lighter!”</p>
    <p class="handle">@RVCarloweDaily</p>
  </article>

  <article class="quote-card card-boost">
    <div class="photo" role="img" aria-label="Photo of RV in a pink dress at a colourful stage event"></div>
    <p class="quote">“A natural way to boost GLP-1 - no injections, no side effects, just real results. Here's how it works”</p>
    <p class="handle">@RVCarloweDaily</p>
  </article>

  <article class="quote-card card-tomorrow">
    <div class="photo" role="img" aria-label="Photo of RV in a sparkly outfit in front of a large basketball in purple light"></div>
    <p class="quote">“Wake up tomorrow with a flatter belly- yes, this overnight remedy works like magic!”</p>
    <p class="handle">@RVCarloweDaily</p>
  </article>
</main>
</body>
</html>
```